Mortgage Loan officer needs clean/modern business card design

Looking for a clean, modern 2-sided business card design. We like the earth tones used in our logo and website http://vukarhome-lending.example . Would also like to incorporate: 1) Something special to make our card stand out - a pop of color or embossed logo, for instance and 2) please include "Mortgage Loans" "Reverse Mortgages" "Private Money Loans" on back of card with the logo.

Front: Needs to include agent/company license info - see website. Agent name: Niall Hargrove

Here are fonts and colors used for our logo:
Font: Avenir Next
Colors:
#2c3539 - Dark Gray
#576870 - Light Gray
#ffffff - Background White

Target Market(s)

Prospects and current clients. Will also be distributing to people in professional network (attorneys and CPAs)

Industry/Entity Type

Business

Contact Information for Business Card

Include agent name, contact info, website on front, licensing info for agent an company. Logo and services offered on back

Font styles to use
Other font styles liked:
• Avenir Next

Requirements
Must have
• See project description
Should not have
• Nothing cheesy

```html
<!DOCTYPE html>
<html lang="en">
<head>
<meta charset="utf-8">
<title>Vukar Home Lending – Business Card</title>
<link rel="stylesheet" href="https://fonts.googleapis.com/css2?family=Nunito+Sans:wght@400;600&display=swap">
<style>
  :root {
    --dark-gray: #2c3539;
    --light-gray: #576870;
    --card-white: #ffffff;
    --backdrop: #e4e4e4;
    --rule: #2c3539;
  }
  * { margin: 0; padding: 0; box-sizing: border-box; }
  html, body {
    width: 1200px; height: 576px; overflow: hidden;
    background: var(--backdrop);
    font-family: "Nunito Sans", sans-serif;
  }
  .stage { position: relative; width: 1200px; height: 576px; }
  .card {
    position: absolute;
    width: 484px; height: 293px;
    background: var(--card-white);
    border-radius: 12px;
    overflow: hidden;
    box-shadow: 0 2px 6px rgba(0,0,0,0.12);
  }
  .card--back  { left: 82px;  top: 139px; }
  .card--front { left: 603px; top: 138px; width: 480px; height: 291px; }

  .brand-ring {
    position: absolute;
    border: 1.5px solid var(--rule);
    border-radius: 50%;
    display: flex; align-items: center; justify-content: center;
    text-align: center;
  }
  .brand-name {
    color: var(--light-gray);
    font-weight: 400;
    line-height: 1.2;
  }
  .card--back .brand-ring { width: 164px; height: 164px; left: 160px; top: 43px; }
  .card--back .brand-name { font-size: 21px; }
  .card--front .brand-ring { width: 132px; height: 132px; left: 48px; top: 80px; }
  .card--front .brand-name { font-size: 17px; }

  .services-band {
    position: absolute; left: 0; top: 248px;
    width: 100%; height: 25px;
    background: var(--dark-gray);
    color: var(--card-white);
    font-size: 12.5px;
    display: flex; align-items: center; justify-content: center;
    gap: 7px;
    letter-spacing: 0.1px;
  }
  .services-band .divider { opacity: 0.9; }

  .agent { position: absolute; left: 220px; top: 78px; }
  .agent-name { color: var(--light-gray); font-weight: 600; font-size: 19.5px; line-height: 1.2; }
  .agent-title { color: var(--dark-gray); font-size: 10.5px; margin-top: 1px; }

  .contact-list { position: absolute; left: 220px; top: 137px; list-style: none; }
  .contact-list li {
    display: flex; align-items: center;
    color: var(--dark-gray); font-size: 12px;
    height: 18.5px;
  }
  .contact-list .icon { width: 10px; height: 10px; margin: 0 13px 0 4px; fill: var(--dark-gray); }
  .contact-list .address { margin-top: 3px; }
</style>
</head>
<body>
<div class="stage">

  <section class="card card--back">
    <div class="brand-ring">
      <span class="brand-name">Vukar Home<br>Lending</span>
    </div>
    <div class="services-band">
      <span>Mortgage Loans</span><span class="divider">|</span>
      <span>Reverse Mortgages</span><span class="divider">|</span>
      <span>Private Money Loans</span>
    </div>
  </section>

  <section class="card card--front">
    <div class="brand-ring">
      <span class="brand-name">Vukar Home<br>Lending</span>
    </div>
    <div class="agent">
      <div class="agent-name">Niall Hargrove</div>
      <div class="agent-title">Owner/Director</div>
    </div>
    <ul class="contact-list">
      <li>
        <svg class="icon" viewBox="0 0 10 10" aria-hidden="true"><path d="M1 3.2C1 2 2.5 1.3 5 1.3S9 2 9 3.2V4H7V3.2H3V4H1Z"/><path d="M2 5h6l1 3.5H1Z"/></svg>
        0400 555 019 27
      </li>
      <li>
        <svg class="icon" viewBox="0 0 10 10" aria-hidden="true"><circle cx="5" cy="5" r="4.3" fill="none" stroke="#2c3539" stroke-width="0.9"/><ellipse cx="5" cy="5" rx="1.8" ry="4.3" fill="none" stroke="#2c3539" stroke-width="0.8"/><path d="M0.8 5h8.4M1.6 3h6.8M1.6 7h6.8" stroke="#2c3539" stroke-width="0.7"/></svg>
        www.vukarhome-lending.example
      </li>
      <li>
        <svg class="icon" viewBox="0 0 10 10" aria-hidden="true"><path d="M0.5 2h9v6h-9Z"/><path d="M0.8 2.3L5 5.6 9.2 2.3" fill="none" stroke="#fff" stroke-width="0.8"/></svg>
        niall@vukarhome-lending.example
      </li>
      <li class="address">118 Larkspur Lane, Marlow NSW 2775</li>
    </ul>
  </section>

</div>
</body>
</html>
```